The Lantern Protocol: A Practical Guide for Tending Old Orchards

This will be for both the hard cover and paperback version. A core theme of the book and what we want to cover to convey is the journey or transformation to "happiness". Concepts such as road/pathway, mountain top, sunrise, dark to bright colors, out-of-focus to in-focus, clouds parting, etc., all represent this idea. I am attaching a 1-page book summary for more information. I like the idea of the subtitle being in a gold seal, but that is not necessary. I am open to any designs, but it should at least be conceptually related to the book.

```html
<!DOCTYPE html>
<html lang="en">
<head>
<meta charset="utf-8">
<title>The Lantern Protocol — Cover</title>
<link rel="stylesheet" href="https://fonts.googleapis.com/css2?family=Marcellus&family=Quicksand:wght@500&display=swap">
<style>
  :root {
    --backdrop: #d6d5d9;
    --cover-dark: #1e1d1c;
    --cover-mid: #2f2d2b;
    --cover-light: #5a5753;
    --slit-light: #e9e9ec;
    --teal: #3fa79c;
    --silver: #b9b9bd;
    --subtitle: #dcdcdf;
  }
  * { margin: 0; padding: 0; box-sizing: border-box; }
  html, body {
    width: 1200px;
    height: 1000px;
    overflow: hidden;
    background: var(--backdrop);
  }
  .book-cover {
    position: absolute;
    left: 320px;
    top: 60px;
    width: 560px;
    height: 880px;
    overflow: hidden;
    background: var(--cover-dark);
  }
  .cover-art {
    position: absolute;
    inset: 0;
    width: 100%;
    height: 100%;
  }
  .title-block {
    position: absolute;
    left: 40px;
    width: 420px;
    top: 92px;
    text-align: center;
    font-family: "Marcellus", serif;
    line-height: 1;
  }
  .title-lead {
    color: var(--teal);
    font-size: 44px;
    letter-spacing: 1px;
  }
  .title-main {
    color: var(--silver);
    font-size: 74px;
    margin-top: 10px;
    letter-spacing: -2px;
  }
  .title-second {
    color: var(--teal);
    font-size: 74px;
    margin-top: 4px;
    letter-spacing: -2px;
  }
  .subtitle {
    margin-top: 28px;
    font-family: "Quicksand", sans-serif;
    font-weight: 500;
    font-size: 25px;
    line-height: 1.6;
    color: var(--subtitle);
  }
  .author {
    position: absolute;
    left: 40px;
    width: 420px;
    top: 790px;
    text-align: center;
    font-family: "Quicksand", sans-serif;
    font-weight: 500;
    font-size: 26px;
    color: var(--teal);
  }
</style>
</head>
<body>
  <main class="book-cover">
    <svg class="cover-art" viewBox="0 0 560 880" preserveAspectRatio="none" role="img" aria-label="Photograph of a dark concrete room with a narrow bright opening in the wall and a lone figure walking toward the light">
      <defs>
        <linearGradient id="room-tone" x1="0" y1="0" x2="1" y2="0">
          <stop offset="0" stop-color="var(--cover-dark)"/>
          <stop offset="0.6" stop-color="var(--cover-mid)"/>
          <stop offset="0.8" stop-color="var(--slit-light)"/>
          <stop offset="0.88" stop-color="var(--cover-light)"/>
          <stop offset="1" stop-color="var(--cover-mid)"/>
        </linearGradient>
        <linearGradient id="floor-shade" x1="0" y1="0" x2="0" y2="1">
          <stop offset="0.6" stop-color="#000" stop-opacity="0"/>
          <stop offset="1" stop-color="#000" stop-opacity="0.45"/>
        </linearGradient>
      </defs>
      <rect width="560" height="880" fill="url(#room-tone)"/>
      <rect width="560" height="880" fill="url(#floor-shade)"/>
    </svg>

    <h1 class="title-block">
      <div class="title-lead">THE</div>
      <div class="title-main">LANTERN</div>
      <div class="title-second">PROTOCOL</div>
      <p class="subtitle">A Practical Guide for Tending<br>Old Orchards</p>
    </h1>

    <p class="author">Martin R. Hale</p>
  </main>
</body>
</html>
```